Einzelne Suchwerk Landingpage
Suchwerk Landingpage für das Thema
„Vergleich von Private Rentenversicherungen“
Haupt Suchbegriffe für die die Landingpage verwendet werden soll:
-Private Rente
-Vergleich Private Rente
-Private Rentenversicherung
Mitbewerber:
Siehe Suchwerk Ergebnisse bei Eingabe obiger Suchbegriffe
Zielgruppe:
Alle Bundesbürger die sich mit privater Altersvorsorge beschäftigen.
Verstärkt Männer aber auch Frauen im Alter zwischen ca. 35-55 J.
Designanforderungen:
Spagat zwischen
Priorität I: ansprechenden des Besuchers auf emotionaler Ebene (Einbindung von Menschenbildern, etc.)
und
Priorität II: Ausdruck von Seriosität, Kompetenz und Unabhängigkeit
Als Beispiel-Designvorlagen von Mitbewerbern finde ich folgende Seite sehr ansprechend:
https://www1.ruhestand-kassenblick.de/ (hier ist mir nur das Formular zu groß, zu wenig Platz für Text)
Oder
http://www.geldlotse17.info/Sofortrente-Vergleich/index.html
(Design ist nicht so toll, aber klar strukturiert)
Vorlage für die Strukturierung der Seite:
Gute Erfahrungen was die Conversionsraten angeht habe ich mit der aktuell schon bestehenden Seite zum Thema „Rürup Rente“ gemacht.
www.kassenblick-basisplan-neu.de
Sicher ist diese was das Design angeht optimierungsfähig.
Was das Verhältnis Text/Formular angeht finde ich den Aufbau jedoch ganz gut bzw. hat sich die Seite bewährt. Die Unterseiten für Datenschutz und Impressum können ebenfalls übernommen werden.
Content
Der Text für die Seite ist hier hinterlegt:
www.wandoret.com/Inhalt_Text.docx
Formular:
Für das Formular könnten Sie ggf. auch den Quelltext der bestehenden Rürup Seite (s.o.) nutzen.
Das müsste dann nur minimal abgeändert werden.
www.wandoret.com/Formular.docx
Bei weiteren Rückfragen stehe ich gerne zur Verfügung.

```html
<!DOCTYPE html>
<html lang="de">
<head>
<meta charset="utf-8">
<title>Private Renten im Vergleich</title>
<link href="https://fonts.googleapis.com/css2?family=Arimo:wght@400;700&display=swap" rel="stylesheet">
<style>
  :root {
    --sky-top: #5f86a6;
    --sky-mid: #b9cad6;
    --ground: #e4e2dc;
    --frame: #f1f1f0;
    --paper: #fcfcfc;
    --accent: #6f9bb8;
    --accent-dark: #5787a8;
    --heading: #6a9ab8;
    --text: #5a5a5a;
    --text-strong: #444;
    --muted: #8a8a8a;
    --rule: #d4d4d4;
    --form-bg: #e9f0f4;
    --field-border: #d6dde2;
    --white: #ffffff;
  }
  * { box-sizing: border-box; margin: 0; padding: 0; }
  html, body { width: 1165px; height: 1200px; overflow: hidden; }
  body {
    font-family: "Arimo", Arial, sans-serif;
    color: var(--text);
    position: relative;
  }
  .backdrop {
    position: absolute; inset: 0;
    background: linear-gradient(180deg, var(--sky-top) 0%, var(--sky-mid) 30%, #d9dde0 55%, var(--ground) 100%);
  }
  .page-frame {
    position: absolute; left: 149px; top: 35px; width: 867px; height: 1101px;
    background: var(--frame);
  }
  .page {
    position: absolute; left: 161px; top: 44px; width: 843px; height: 1084px;
    background: var(--paper);
  }
  .abs { position: absolute; }

  .top-nav {
    right: 171px; top: 57px; font-size: 10.5px; letter-spacing: .3px;
    color: var(--muted); text-transform: uppercase;
  }
  .site-name {
    left: 176px; top: 79px; font-size: 22px; color: var(--heading); font-weight: 400;
  }
  .hero {
    left: 172px; top: 128px; width: 821px; height: 159px;
    background: linear-gradient(90deg, #7f9fb7 0%, #a9c1d1 40%, #c7d6df 62%, #d9c8b0 80%, #b9a58a 100%);
  }
  .hero-title {
    left: 188px; top: 221px; font-size: 21px; line-height: 23px; color: var(--white); font-weight: 400;
  }
  .notice {
    left: 172px; top: 295px; width: 821px; height: 45px; background: var(--accent);
    display: flex; align-items: center; padding-left: 17px; gap: 22px;
    color: var(--white); font-size: 11.5px; font-weight: 700;
  }
  .notice strong { margin-right: 6px; }

  .content { left: 172px; top: 359px; width: 452px; font-size: 9.5px; line-height: 16px; }
  .content p { margin-bottom: 7px; }
  .content .lead { font-weight: 700; color: var(--text-strong); margin-bottom: 16px; }
  .content h3 { font-size: 9.5px; color: var(--heading); font-weight: 700; margin: 14px 0 6px; }
  .content h4 { font-size: 9.5px; color: var(--text-strong); font-weight: 700; margin: 14px 0 3px; }
  .content ul { list-style: none; margin: 12px 0 0 14px; }
  .content li { display: flex; align-items: center; gap: 9px; }
  .content li svg { flex: none; }

  .compare { left: 662px; top: 362px; width: 331px; }
  .compare .eyebrow { font-size: 9px; font-weight: 700; color: var(--accent-dark); }
  .compare h2 { font-size: 16.5px; color: var(--accent-dark); font-weight: 700; line-height: 19px; }
  .compare .intro { font-size: 9.5px; margin-top: 9px; padding-bottom: 9px; border-bottom: 1px solid #bdbdbd; }
  .compare .intro span { color: var(--accent-dark); }

  .quote-form {
    left: 662px; top: 428px; width: 331px; height: 425px; background: var(--form-bg);
    padding: 15px 19px 0 19px;
  }
  .field-row { display: flex; align-items: center; height: 26.5px; }
  .field-row label { width: 137px; font-size: 9.5px; color: var(--accent-dark); }
  .controls { display: flex; gap: 5px; width: 156px; }
  .box {
    height: 20px; background: var(--white); border: 1px solid var(--field-border); position: relative;
  }
  .select::after {
    content: ""; position: absolute; right: 6px; top: 8px;
    border-left: 3px solid transparent; border-right: 3px solid transparent; border-top: 4px solid #9aaab6;
  }
  .w-full { width: 156px; } .w-half { width: 75.5px; } .w-third { width: 48.7px; }
  .w-wide { width: 102px; } .w-narrow { width: 49px; }
  .consent { display: flex; gap: 13px; margin: 13px 0 0 137px; font-size: 9.5px; line-height: 15px; }
  .consent .tick-box { width: 11px; height: 11px; border: 1px solid var(--field-border); background: var(--white); margin-top: 2px; flex: none; }
  .consent b { color: var(--accent-dark); }
  .send {
    margin: 12px 0 0 137px; width: 70px; height: 20px; background: var(--accent);
    color: var(--white); font-size: 10px; letter-spacing: .4px; display: flex; align-items: center; justify-content: center;
  }

  .next-steps { left: 662px; top: 872px; width: 331px; font-size: 9.5px; line-height: 16px; color: var(--muted); }
  .next-steps h5 { font-size: 9.5px; font-weight: 400; text-decoration: underline; margin-bottom: 6px; }
  .next-steps p { margin-bottom: 6px; }
  .next-steps p.gap { margin-top: 16px; }

  .footer-rule { left: 172px; top: 1083px; width: 821px; height: 1px; background: var(--rule); }
  .footer-links { left: 172px; top: 1099px; font-size: 9.5px; color: var(--muted); }
  .copyright { right: 172px; top: 1099px; font-size: 9.5px; color: var(--muted); }
</style>
</head>
<body>
  <div class="backdrop" role="img" aria-label="Heller Wolkenhimmel als Seitenhintergrund"></div>
  <div class="page-frame"></div>
  <div class="page"></div>

  <div class="abs top-nav">Altersvorsorge / Private Rentenversicherungen</div>
  <div class="abs site-name">www.rentenblick-vergleich.com</div>

  <div class="abs hero" role="img" aria-label="Lächelndes älteres Paar vor Meereshintergrund"></div>
  <h1 class="abs hero-title">Welche Private Rentenversicherung<br>soll ich nehmen?</h1>

  <div class="abs notice">
    <svg width="22" height="18" viewBox="0 0 22 18" aria-hidden="true">
      <path d="M7 1h13a1 1 0 0 1 1 1v8a1 1 0 0 1-1 1h-2v3l-3-3H7a1 1 0 0 1-1-1V2a1 1 0 0 1 1-1z" fill="#fff" opacity=".75"/>
      <path d="M2 4h12a1 1 0 0 1 1 1v7a1 1 0 0 1-1 1H7l-3 3v-3H2a1 1 0 0 1-1-1V5a1 1 0 0 1 1-1z" fill="#fff"/>
    </svg>
    <div><strong>ACHTUNG!</strong> Bis 31.12.2011 noch höhere Garantieverzinsung für die gesamte Laufzeit sichern! Jetzt einfach Renten vergleichen!</div>
  </div>

  <main class="abs content">
    <p class="lead">Bevor Sie sich für die Private Rentenversicherung eines bestimmten Anbieters entscheiden, sollten Sie wissen, was vergleichbare Rentenversicherungen leisten. Welcher Anbieter für Sie attraktiv ist, kann nämlich je nach Eintrittsalter, Geschlecht oder Anlagementalität sehr variieren.</p>
    <p>Der Vergleich lohnt sich für Sie, denn gerade bei Privaten Rentenversicherungen gibt es riesige Unter-schiede. Selbst wenn Ihnen die Differenz bei den Rentenergebnissen der Anbieter eher klein erscheint, können sich über die gesamte Rentenphase Unterschiede von 10.000 EUR und mehr ergeben.</p>
    <h3>Als unabhängige Vorsorgespezialisten holen wir mehr für Sie heraus!</h3>
    <p>Fordern Sie jetzt Ihren kostenlosen und unverbindlichen Marktvergleich an. Unser Marktvergleich bietet mehr...</p>
    <ul class="ticks">
      <li><svg width="10" height="9" viewBox="0 0 10 9"><path d="M1 5l3 3 5-7" stroke="#888" stroke-width="1.6" fill="none"/></svg>Vergleich von über 45 Versicherungen</li>
      <li><svg width="10" height="9" viewBox="0 0 10 9"><path d="M1 5l3 3 5-7" stroke="#888" stroke-width="1.6" fill="none"/></svg>Klassische- und Fondsprodukte</li>
      <li><svg width="10" height="9" viewBox="0 0 10 9"><path d="M1 5l3 3 5-7" stroke="#888" stroke-width="1.6" fill="none"/></svg>Inkl. Direktversicherer</li>
      <li><svg width="10" height="9" viewBox="0 0 10 9"><path d="M1 5l3 3 5-7" stroke="#888" stroke-width="1.6" fill="none"/></svg>Inkl. berufsspezifischer Sonderrabatttarife</li>
      <li><svg width="10" height="9" viewBox="0 0 10 9"><path d="M1 5l3 3 5-7" stroke="#888" stroke-width="1.6" fill="none"/></svg>Tarife mit vergünstigten Kosten</li>
    </ul>
    <h4 style="margin-top:18px">Das gesetzliche Rentenniveau genügt nicht zur Grundversorgung!</h4>
    <p>Mittlerweile ist es fast jedem klar. Die gesetzliche Rente wird nicht zur Grundversorgung ausreichen.<br>Daher ist private Vorsorge unausweichlich.<br>Jedoch unterschätzen die meisten Bundesbürger die Höhe der Rentenlücke im Alter.</p>
    <h3 style="margin-top:17px">Folgende Faktoren werden meist unterschätzt:</h3>
    <ul class="arrows">
      <li><svg width="6" height="7" viewBox="0 0 6 7"><path d="M0 0l6 3.5L0 7z" fill="#aaa"/></svg>Hohe Inflation</li>
      <li><svg width="6" height="7" viewBox="0 0 6 7"><path d="M0 0l6 3.5L0 7z" fill="#aaa"/></svg>Immer weiter steigende Sozialabgaben</li>
      <li><svg width="6" height="7" viewBox="0 0 6 7"><path d="M0 0l6 3.5L0 7z" fill="#aaa"/></svg>Insbesondere Krankenversicherungsausgaben</li>
      <li><svg width="6" height="7" viewBox="0 0 6 7"><path d="M0 0l6 3.5L0 7z" fill="#aaa"/></svg>Steigende Lebenshaltungskosten</li>
      <li><svg width="6" height="7" viewBox="0 0 6 7"><path d="M0 0l6 3.5L0 7z" fill="#aaa"/></svg>Pflegekosten</li>
      <li><svg width="6" height="7" viewBox="0 0 6 7"><path d="M0 0l6 3.5L0 7z" fill="#aaa"/></svg>etc.</li>
    </ul>
    <h3 style="margin-top:17px">Die Vorteile der privaten Rentenversicherung:</h3>
    <ul class="plus">
      <li><svg width="8" height="8" viewBox="0 0 8 8"><path d="M4 0v8M0 4h8" stroke="#888" stroke-width="1.4"/></svg>Maximale Flexibilität</li>
      <li><svg width="8" height="8" viewBox="0 0 8 8"><path d="M4 0v8M0 4h8" stroke="#888" stroke-width="1.4"/></svg>Beliebige Vererbbarkeit</li>
      <li><svg width="8" height="8" viewBox="0 0 8 8"><path d="M4 0v8M0 4h8" stroke="#888" stroke-width="1.4"/></svg>Wahlrecht Kapital oder Rente</li>
      <li><svg width="8" height="8" viewBox="0 0 8 8"><path d="M4 0v8M0 4h8" stroke="#888" stroke-width="1.4"/></svg>Garantierte lebenslange Rente</li>
      <li><svg width="8" height="8" viewBox="0 0 8 8"><path d="M4 0v8M0 4h8" stroke="#888" stroke-width="1.4"/></svg>Abgeltungssteuerfrei sparen</li>
      <li><svg width="8" height="8" viewBox="0 0 8 8"><path d="M4 0v8M0 4h8" stroke="#888" stroke-width="1.4"/></svg>Attraktive Rendite mit Garantieverzinsung</li>
    </ul>
  </main>

  <section class="abs compare">
    <div class="eyebrow">Private Rente: Anbieter &amp; Tarife</div>
    <h2>Private Renten im Vergleich</h2>
    <p class="intro">Fordern Sie hier Ihren <span>kostenlosen</span> Versicherungsvergleich an.</p>
  </section>

  <form class="abs quote-form">
    <div class="field-row"><label>Anlagebetrag (€) / Zahlart</label><div class="controls"><span class="box w-half"></span><span class="box select w-half"></span></div></div>
    <div class="field-row"><label>Rentenauszahlung (Alter)</label><div class="controls"><span class="box w-full"></span></div></div>
    <div class="field-row"><label>Bruttoeinkommen (€/Jahr)</label><div class="controls"><span class="box w-full"></span></div></div>
    <div class="field-row"><label>Kinder</label><div class="controls"><span class="box select w-full"></span></div></div>
    <div class="field-row"><label>Familienstand</label><div class="controls"><span class="box select w-full"></span></div></div>
    <div class="field-row"><label>Beruf / Berufsstatus</label><div class="controls"><span class="box w-half"></span><span class="box select w-half"></span></div></div>
    <div class="field-row"><label>Geburtsdatum</label><div class="controls"><span class="box select w-third"></span><span class="box select w-third"></span><span class="box select w-third"></span></div></div>
    <div class="field-row"><label>Anrede / Vorname / Name</label><div class="controls"><span class="box select w-third"></span><span class="box w-third"></span><span class="box w-third"></span></div></div>
    <div class="field-row"><label>Straße / Hausnummer</label><div class="controls"><span class="box w-wide"></span><span class="box w-narrow"></span></div></div>
    <div class="field-row"><label>PLZ, Wohnort</label><div class="controls"><span class="box w-narrow"></span><span class="box w-wide"></span></div></div>
    <div class="field-row"><label>Tel.-Nr. / Erreichbarkeit</label><div class="controls"><span class="box w-half"></span><span class="box select w-half"></span></div></div>
    <div class="field-row"><label>eMail-Adresse</label><div class="controls"><span class="box w-full"></span></div></div>
    <div class="consent"><span class="tick-box"></span><span>Ich habe den <b>Datenschutz</b><br>gelesen und akzeptiert.</span></div>
    <div class="send">SENDEN</div>
  </form>

  <aside class="abs next-steps">
    <h5>Sie haben Ihre Angaben gemacht. So geht es weiter:</h5>
    <p>In Kürze erhalten Sie Ihren Versicherungsvergleich. Der Vergleich wird softwaregestützt von unseren qualifizierten Spezialisten erstellt.</p>
    <p>Dieser Service ist kostenfrei. Wir bitten Sie nur ernsthafte und vollständige Angaben zu machen, da ansonsten kein Vergleich erstellt werden kann.</p>
    <p class="gap">Bei weiteren Fragen stehen Ihnen unsere Experten via Onlineberatung zur Verfügung.</p>
  </aside>

  <div class="abs footer-rule"></div>
  <div class="abs footer-links">Impressum I Datenschutz</div>
  <div class="abs copyright">Copyright © 2011 www.rentenblick-vergleich.com . Alle Rechte vorbehalten.</div>
</body>
</html>
```